Customer Value Leaflet

We need a bi-fold brochure designing, based on the attached PDF wireframes. Our company name is mistralgrove.com (of which the logo is currently being designed). The corporate colour is orange (the exact shade of which we are happy to leave to the designers discretion).

The leaflet will distributed to customer experience experts and marketers so the design needs to be bright, engaging, clean and simple. Design is critical.

Industry/Entity Type

It Company

```html
<!DOCTYPE html>
<html lang="en">
<head>
<meta charset="utf-8">
<title>Customer Lifetime Value Leaflet</title>
<link href="https://fonts.googleapis.com/css2?family=Open+Sans:wght@400;600;700;800&display=swap" rel="stylesheet">
<style>
:root{
  --navy:#2e3f74;
  --orange:#f07d1a;
  --orange-light:#ffab4d;
  --white:#ffffff;
  --shadow:#1b1f2e;
  --ring:#c8cde0;
}
*{margin:0;padding:0;box-sizing:border-box}
html,body{width:1200px;height:849px;overflow:hidden;background:var(--white)}
body{font-family:"Open Sans",Arial,sans-serif;color:var(--navy)}
.leaflet{position:relative;width:1200px;height:849px}

.cover{position:absolute;left:0;top:0;width:600px;height:849px;
  background:
    linear-gradient(180deg,rgba(0,0,0,0) 55%,rgba(60,35,20,.35) 100%),
    linear-gradient(125deg,#f4f1ee 0%,#c9a07a 18%,#e8c2a6 38%,#d9a98b 55%,#b88a70 72%,#e9e4e0 92%,#f6f6f6 100%)}
.cover-accent{position:absolute;left:40px;top:662px;width:48px;height:4px;background:var(--orange)}
.cover-text{position:absolute;left:40px;top:676px;color:var(--white)}
.cover-head{font-weight:700;font-size:19px;line-height:23px}
.cover-sub{font-weight:700;font-size:14.5px;line-height:17px;margin-top:13px}
.cover-link{font-size:15px;margin-top:17px}
.cover-link b{font-weight:700;color:var(--orange-light)}

.avatar{position:absolute;width:100px;height:100px;border-radius:50%;
  background:linear-gradient(135deg,var(--navy) 0%,var(--orange) 100%);padding:5px}
.avatar span{display:block;width:100%;height:100%;border-radius:50%;background:#eef0f4}
.meet{position:absolute;top:144px;width:200px;font-weight:800;font-size:19px;color:var(--navy);letter-spacing:.3px;text-align:center}

.profile{position:absolute;top:180px;width:190px;height:167px;background:var(--navy);
  box-shadow:3px 3px 0 var(--shadow);color:var(--white);font-size:15px;line-height:17.2px;padding:13px 18px}
.banner{position:absolute;left:642px;top:372px;width:518px;height:44px;background:var(--navy);
  box-shadow:3px 3px 0 var(--shadow);color:var(--white);font-size:18px;line-height:44px;padding-left:16px}

.timeline{position:absolute;left:866px;top:432px}
.step-icon{position:absolute;width:72px;height:72px;border-radius:50%;background:var(--navy);
  box-shadow:0 0 0 2px var(--white),0 0 0 3px var(--ring)}
.step-icon svg{position:absolute;left:16px;top:16px}
.brand-word{position:absolute;left:0;top:0;width:72px;height:72px;line-height:72px;text-align:center;
  color:var(--white);font-size:11px;font-weight:700}
.step-text{position:absolute;font-size:12.5px;line-height:14.5px;color:var(--navy);white-space:nowrap}
.divider{position:absolute;height:0;border-top:1.5px dashed var(--orange);width:186px}

.verdict{position:absolute;left:777px;top:762px;width:248px;height:44px;background:var(--navy);
  box-shadow:3px 3px 0 var(--orange);color:var(--white);font-size:18px;line-height:44px;text-align:center}
</style>
</head>
<body>
<div class="leaflet">
  <section class="cover" role="img" aria-label="Photograph of a smiling customer service agent wearing a headset">
    <div class="cover-accent"></div>
    <div class="cover-text">
      <p class="cover-head">By predicting<br>Customer Lifetime Value today…</p>
      <p class="cover-sub">…you can optimise your business<br>for tomorrow</p>
      <p class="cover-link">Find our more at <b>www.mistralgrove.com</b></p>
    </div>
  </section>

  <div class="avatar" style="left:723px;top:42px" role="img" aria-label="Illustration of Kim"><span></span></div>
  <div class="avatar" style="left:977px;top:42px" role="img" aria-label="Illustration of Kevin"><span></span></div>
  <h2 class="meet" style="left:673px">MEET KIM</h2>
  <h2 class="meet" style="left:927px">MEET KEVIN</h2>

  <p class="profile" style="left:680px">Kim has purchased<br>3 items from you<br>over the past 3<br>months @ £109<br>margin and you<br>acquired her though<br>a Searchly PPC<br>campaign</p>
  <p class="profile" style="left:932px">Kevin purchased<br>an item last week<br>@ £31 margin and<br>you acquired him<br>though a retargeting<br>campaign</p>

  <p class="banner">Right now you probably think Kim is your best customer…</p>

  <svg class="timeline" width="70" height="320" viewBox="0 0 70 320" aria-label="Timeline: plus 6 months, plus 1 month, plus 1 week">
    <defs><linearGradient id="flow" x1="0" y1="0" x2="0" y2="1">
      <stop offset="0" stop-color="#d9650c"/><stop offset="1" stop-color="#ffa040"/></linearGradient></defs>
    <path d="M14 0H56V278H68L35 318L2 278H14Z" fill="url(#flow)"/>
    <text transform="translate(41 288) rotate(-90)" fill="#fff" font-family="Open Sans,Arial,sans-serif" font-weight="700" font-size="14" textLength="280" lengthAdjust="spacing" xml:space="preserve">+ 6 MONTHS  + 1 MONTH   + 1 WEEK</text>
  </svg>

  <div class="step-icon" style="left:679px;top:438px">
    <svg width="40" height="40" viewBox="0 0 40 40" fill="none" stroke="#fff" stroke-width="2.2"><path d="M4 8h20v12H12l-5 5v-5H4z"/><path d="M16 22v4h12l5 5v-5h3V14h-9"/></svg>
  </div>
  <p class="step-text" style="left:768px;top:441px">Kim calls you<br>to return an<br>item…</p>
  <div class="divider" style="left:679px;top:522px"></div>

  <div class="step-icon" style="left:679px;top:537px">
    <svg width="40" height="40" viewBox="0 0 40 40" fill="none" stroke="#fff" stroke-width="2.4"><path d="M3 8h5l4 16h18l4-12H10"/><circle cx="14" cy="30" r="2.5" fill="#fff"/><circle cx="27" cy="30" r="2.5" fill="#fff"/></svg>
  </div>
  <p class="step-text" style="left:768px;top:542px">Places 4 more<br>online orders…</p>
  <div class="divider" style="left:679px;top:623px"></div>

  <div class="step-icon" style="left:679px;top:638px">
    <svg width="40" height="40" viewBox="0 0 40 40" fill="#fff"><path d="M27 5l8 8-18 18-9 2 2-9z"/></svg>
  </div>
  <p class="step-text" style="left:768px;top:643px">Then places<br>another order<br>but doesn't<br>come back for<br>a month</p>

  <div class="step-icon" style="left:932px;top:438px">
    <svg width="40" height="40" viewBox="0 0 40 40" fill="#fff"><rect x="7" y="4" width="26" height="32" rx="2"/><rect x="10" y="7" width="20" height="7" fill="#2e3f74"/><g fill="#2e3f74"><rect x="10" y="17" width="4" height="3"/><rect x="16" y="17" width="4" height="3"/><rect x="22" y="17" width="4" height="3"/><rect x="10" y="23" width="4" height="3"/><rect x="16" y="23" width="4" height="3"/><rect x="22" y="23" width="4" height="3"/><rect x="10" y="29" width="4" height="3"/><rect x="16" y="29" width="4" height="3"/><rect x="22" y="29" width="4" height="3"/></g></svg>
  </div>
  <p class="step-text" style="left:1021px;top:441px">Kevin makes<br>another<br>purchase…</p>
  <div class="divider" style="left:932px;top:522px"></div>

  <div class="step-icon" style="left:932px;top:537px"><span class="brand-word">Chirpio</span></div>
  <p class="step-text" style="left:1021px;top:542px">Then 2 more<br>(and even tweets<br>about how great<br>your service is)…</p>
  <div class="divider" style="left:932px;top:623px"></div>

  <div class="step-icon" style="left:932px;top:638px">
    <svg width="40" height="40" viewBox="0 0 40 40" fill="none" stroke="#fff" stroke-width="2.4"><path d="M3 8h5l4 16h18l4-12H10"/><circle cx="14" cy="30" r="2.5" fill="#fff"/><circle cx="27" cy="30" r="2.5" fill="#fff"/></svg>
  </div>
  <p class="step-text" style="left:1021px;top:643px">And continues to<br>make purchases<br>on a bi-monthly<br>basis</p>

  <p class="verdict">but really it is Kevin.</p>
</div>
</body>
</html>
```